BRIGHT COLORFUL + 55 FAMILY HISTORY BROCHURE 11 x 17 bifold

11 x 17 Bifold Flyer I have given you the Layout I just need you to make it Pretty

YOU DO NOT NEED TO FOLLOW MY LAYOUT, You can but dont have too

Target Market(s)

55 year old consumers, who could choose our service of Hereditary Cancer Screening

Industry/Entity Type

Health And Wellness

Requirements
Must have
• Must be appealing to Grand Parents, must make them want to test , show lots of pictures of grand children, YOU DO NOT NEED TO FOLLOW MY LAYOUT , You can but dont have too
Nice to have
• use our colors of our logo , YOU DO NOT NEED TO FOLLOW MY LAYOUT , You can but dont have too
Should not have
• YOU DO NOT NEED TO FOLLOW MY LAYOUT, You can but dont have too

```html
<!DOCTYPE html>
<html lang="en">
<head>
<meta charset="utf-8">
<title>Hereditary Cancer Screening Brochure</title>
<link href="https://fonts.googleapis.com/css2?family=Oswald:wght@400;500;600&family=Open+Sans:wght@400;600;700&display=swap" rel="stylesheet">
<style>
:root{
  --navy:#1f3a6e;
  --green:#7cc242;
  --ink:#4a4f57;
  --paper:#ffffff;
  --bg:#e6dcd6;
  --photo-warm:#d9b79a;
  --photo-soft:#e8d3c2;
  --photo-park:#8fae6a;
}
*{box-sizing:border-box;margin:0;padding:0}
html,body{width:1200px;height:1200px;overflow:hidden;background:var(--bg);font-family:"Open Sans",sans-serif;color:var(--ink)}
.spread{position:absolute;left:175px;width:850px;height:550px;display:flex;box-shadow:0 6px 18px rgba(0,0,0,.12)}
.spread.outer{top:30px}
.spread.inner{top:620px}
.page{position:relative;width:425px;height:550px;background:var(--paper);overflow:hidden}
.page.left{box-shadow:inset -10px 0 14px -12px rgba(0,0,0,.25)}
.page.right{box-shadow:inset 10px 0 14px -12px rgba(0,0,0,.2)}
.photo{position:absolute;border-radius:2px}
.photo.warm{background:linear-gradient(135deg,var(--photo-soft),var(--photo-warm))}
.photo.park{background:linear-gradient(135deg,#b9cf8e,var(--photo-park) 60%,#c9d8ea)}
.sq{position:absolute}
.sq.navy{background:var(--navy)}
.sq.green{background:var(--green)}
.brand{position:absolute;display:flex;align-items:center;gap:6px;font-family:"Oswald",sans-serif;font-weight:500;color:var(--navy);font-size:14px;line-height:1.05;text-transform:uppercase;letter-spacing:.5px}
.brand .dot{width:22px;height:22px;border-radius:50%;background:var(--green)}
.url-bar{position:absolute;height:16px;background:var(--navy);color:#fff;font-size:8px;letter-spacing:2.5px;display:flex;align-items:center;justify-content:center}
.url{position:absolute;color:var(--navy);font-size:7.5px;letter-spacing:1px;font-weight:600;white-space:nowrap}
h2,h3{font-family:"Oswald",sans-serif;font-weight:500}
.green{color:var(--green)}
.navy-t{color:var(--navy)}
p{font-size:7.2px;line-height:1.45}
p b{color:#2b2f36}
.title-h{position:absolute;left:150px;top:258px;font-family:"Oswald",sans-serif;font-weight:600;color:var(--green);font-size:40px;letter-spacing:.5px;line-height:1}
.title-s{position:absolute;left:150px;top:303px;font-family:"Oswald",sans-serif;font-weight:500;color:var(--navy);font-size:24px;line-height:1}
</style>
</head>
<body>

<section class="spread outer">
  <article class="page left back-cover">
    <div class="sq green" style="left:82px;top:58px;width:40px;height:40px"></div>
    <div class="photo warm" role="img" aria-label="Grandfather and grandchild photo" style="left:126px;top:44px;width:100px;height:64px"></div>
    <div class="photo warm" role="img" aria-label="Grandmother hugging grandchildren photo" style="left:40px;top:102px;width:82px;height:64px"></div>
    <div class="sq navy" style="left:126px;top:112px;width:40px;height:40px"></div>
    <div class="photo warm" role="img" aria-label="Grandmother and grandchild smiling photo" style="left:40px;top:170px;width:100px;height:62px"></div>
    <div class="brand" style="left:40px;top:262px"><span class="dot"></span><span>Kinwell<br>Health Group</span></div>
    <h3 class="navy-t" style="position:absolute;left:40px;top:312px;font-size:13px">DOES CANCER Run in Your Family?</h3>
    <h3 class="green" style="position:absolute;left:40px;top:330px;font-size:12px">A Simple Swab Could SAVE a Family Members LIFE</h3>
    <p class="navy-t" style="position:absolute;left:40px;top:352px;width:330px;font-size:8px">Your decision won't just affect you. It will also impact Your Family, since your test results may Forecast Their Cancer Risks, too.</p>
    <p style="position:absolute;left:40px;top:388px;width:345px;font-size:8.5px;font-weight:700;color:#2b2f36">We believe it is important to understand what can and cannot be learned with genetic testing.</p>
    <p style="position:absolute;left:40px;top:418px;width:345px;font-size:6px">Genetic mutations can increase risks for certain cancers, but this does not mean cancer will develop. Be prepared to receive positive or negative results. Most people receive negative results, meaning no mutations linked to hereditary cancers were found.</p>
    <div class="url-bar" style="left:40px;top:462px;width:250px">www.kinwellscreening.com</div>
  </article>

  <article class="page right front-cover">
    <div class="brand" style="left:255px;top:28px"><span class="dot"></span><span>Kinwell<br>Health Group</span></div>
    <div class="sq navy" style="left:110px;top:70px;width:34px;height:34px"></div>
    <div class="photo warm" role="img" aria-label="Three generation family photo" style="left:30px;top:108px;width:100px;height:48px"></div>
    <div class="photo warm" role="img" aria-label="Grandparents with grandchildren photo" style="left:150px;top:92px;width:80px;height:52px"></div>
    <div class="sq navy" style="left:236px;top:80px;width:32px;height:32px"></div>
    <div class="sq green" style="left:236px;top:118px;width:34px;height:34px"></div>
    <div class="sq navy" style="left:276px;top:104px;width:32px;height:32px"></div>
    <div class="sq navy" style="left:112px;top:160px;width:28px;height:28px"></div>
    <div class="photo warm" role="img" aria-label="Large family gathering photo" style="left:150px;top:150px;width:80px;height:50px"></div>
    <div class="photo warm" role="img" aria-label="Grandfather carrying grandchild photo" style="left:282px;top:140px;width:110px;height:62px"></div>
    <div class="sq green" style="left:112px;top:194px;width:26px;height:22px"></div>
    <div class="photo warm" role="img" aria-label="Family dinner photo" style="left:150px;top:206px;width:80px;height:40px"></div>
    <div class="sq green" style="left:282px;top:208px;width:36px;height:30px"></div>
    <div class="sq navy" style="left:324px;top:206px;width:30px;height:30px"></div>
    <div class="title-h">HEREDITARY</div>
    <div class="title-s">Cancer Screening</div>
    <div style="position:absolute;left:150px;top:334px;font-size:11px;font-weight:700;color:#2b2f36">"The Test You Take For Them"</div>
    <p style="position:absolute;left:150px;top:353px;width:260px;font-size:6px">Will you give your loved ones the information to beat cancer in their lives? Give them the gift of knowledge.</p>
    <div class="green" style="position:absolute;left:150px;top:374px;font-size:9px;font-weight:700">knowing is better than not knowing. Knowledge is Power</div>
    <div class="url-bar" style="left:150px;top:398px;width:240px">www.kinwellscreening.com</div>
  </article>
</section>

<section class="spread inner">
  <article class="page left">
    <div class="sq navy" style="left:30px;top:50px;width:22px;height:18px"></div>
    <h2 class="navy-t" style="position:absolute;left:30px;top:70px;width:380px;font-size:21px;line-height:1.1">A Positive result or finding a mutation is Not a Cancer Diagnosis</h2>
    <h3 class="green" style="position:absolute;left:30px;top:126px;width:370px;font-size:11.5px;line-height:1.25;font-family:'Open Sans',sans-serif;font-weight:700">and does not mean you will ever develop Cancer learning if you have an increased risk for cancer can make a difference</h3>
    <div style="position:absolute;left:30px;top:168px;width:175px">
      <p><b>Genetic testing revealed</b> Daniel Mercer carried a mutation that gave him a 55 to 70 percent chance of developing stomach cancer. Early screening revealed there were 14 sites of stage 1A cancer. Once the news sunk in, he realized his mother's genetic testing saved his life.</p>
      <p style="margin-top:8px"><b>Genetic Testing Saved My Life.</b> Because of my age and ancestry, my doctor recommended genetic testing, and they were right. I had the gene, and my sister did too. Now we are in control; there are steps that can be taken to reduce the risk, including enhanced breast cancer screening, risk-reducing surgeries and chemoprevention to try to reduce the risk or delay the development of cancer.</p>
    </div>
    <div style="position:absolute;left:220px;top:168px;width:180px">
      <p><b>A breast cancer survivor before age 30:</b> Genetic testing saved my life, Carla Hayes. I was diagnosed with breast cancer two weeks before her 29th birthday. Now 30, she credits her recovery to awareness of a hereditary genetic mutation that predisposed her to the disease. After my mom tested positive for the gene mutation, I knew genetic testing was something I should do. Once I tested positive, I was referred to a breast health clinic for increased surveillance. Knowledge is power, and in this case it watched closely.</p>
      <p style="margin-top:8px"><b>My father had genetic testing</b> and found he had hereditary nonpolyposis colorectal cancer. My name is Ruth Ellison and I am a 10-year survivor of colorectal cancer. From an early age I learned the importance of screenings and knew about signs and symptoms. Following screening guidelines for individuals at increased risk and knowing my family history saved my life!</p>
    </div>
    <div class="photo warm" role="img" aria-label="Mother, grandmother and baby smiling photo" style="left:30px;top:430px;width:200px;height:100px"></div>
    <div class="sq green" style="left:236px;top:425px;width:38px;height:34px"></div>
    <div class="sq navy" style="left:236px;top:464px;width:38px;height:38px"></div>
    <div class="url" style="left:282px;top:490px">www.kinwellscreening.com</div>
  </article>

  <article class="page right">
    <div class="sq navy" style="left:22px;top:42px;width:24px;height:16px"></div>
    <h2 class="navy-t" style="position:absolute;left:22px;top:44px;width:360px;font-size:18px;line-height:1.15;text-indent:30px">There are many Known risk factors for Cancer. <span class="green">GENETICS</span> and <span class="green">FAMILY HISTORY</span> are Often Overlooked.</h2>
    <div style="position:absolute;left:30px;top:128px;width:175px">
      <p><b>Genetic Testing</b> is done to determine whether family members without obvious illness have inherited the same mutation as a family member who is known to carry a cancer associated mutation, meaning will you help your kids and grand children.</p>
      <p style="margin-top:6px"><b>What are the benefits of testing?</b> "The Power of Knowledge" helping younger family members know if there is a risk and preparing for it. Knowing you have a genetic mutation means you can work with your doctor to monitor and address your cancer risks. According to the National Wellness Council, eating 5 or more servings of vegetables and fruit, and most importantly lowering your intake of red meat, dairy and eggs will help prevent or delay cancer.</p>
    </div>
    <div style="position:absolute;left:218px;top:128px;width:180px">
      <p><b>There are many benefits to getting tested,</b> regardless of the eventual result. If one of your family members, however distant, had cancer, there is a chance that you inherited a gene mutation that not only increases your personal risk of cancer, but could also be passed to the next generation. Those who carry hereditary gene mutations could be at risk of getting cancer earlier in life than the general population. <b>The sooner genetic testing is done, the more likely it is that the risk can be managed appropriately.</b></p>
    </div>
    <div class="brand" style="left:300px;top:288px;font-size:11px"><span class="dot" style="width:18px;height:18px"></span><span>Kinwell<br>Health Group</span></div>
    <div class="photo park" role="img" aria-label="Three generation family in a park photo" style="left:22px;top:338px;width:380px;height:150px"></div>
  </article>
</section>

</body>
</html>
```